Post Surgery Care Reminder App

Mobile app-based reminder for patients after surgery. Often times once the patient goes home, they are instructed to take medications and perform other care for their wounds. This app will be designed to help patients keep on top of their care to ensure optimal outcomes after their surgery. See the attached video link (clipvane) in the "Must Haves" section for example of our current beta version.

We have immediate room for improvements from the version in the video; looking for designer/coder to help us complete this project to move to consumers.

Target Market(s)

Patients undergoing elective surgeries

Industry/Entity Type

Health Care

Colors

Designer to choose colors to be used in the design.

Requirements
Must have
• Please see linked clipvane video for demonstration:
• https://www.clipvane.com/watch?v=Rk7pLw2qXzN
Nice to have
• Improved user interface: pleasing to the eye as well as smooth and easy to navigate experience.

```html
<!DOCTYPE html>
<html lang="en">
<head>
<meta charset="utf-8">
<title>Post Surgery Care Reminder</title>
<link href="https://fonts.googleapis.com/css2?family=Roboto:wght@400;500&display=swap" rel="stylesheet">
<style>
  :root {
    --page-bg: #d9efe6;
    --screen-bg: #f3f4f9;
    --status-blue: #0073c6;
    --kit-red: #f44336;
    --kit-red-deep: #e8392e;
    --card-white: #ffffff;
    --text-grey: #4a4a4a;
    --btn-green: #00c47a;
    --btn-teal: #00a6c8;
    --btn-blue: #0068c4;
    --clock-green: #3dcc63;
    --clock-cream: #f6efd8;
  }
  * { box-sizing: border-box; margin: 0; padding: 0; }
  html, body {
    width: 1200px; height: 1200px; overflow: hidden;
    background: var(--page-bg);
    font-family: "Roboto", sans-serif;
  }
  .app-screen {
    position: absolute; left: 269px; top: 10px;
    width: 576px; height: 1027px;
    transform: scale(1.15); transform-origin: top left;
    background: var(--screen-bg);
    box-shadow: 0 4px 24px rgba(0,0,0,0.08);
  }
  .status-bar {
    height: 38px; background: var(--status-blue);
    display: flex; align-items: center; justify-content: flex-end;
    gap: 8px; padding-right: 12px;
    color: #fff; font-size: 21px;
  }
  .status-bar .time { margin-left: 6px; }
  .care-kit-art {
    position: absolute; left: 179px; top: 124px;
    width: 224px; height: 202px;
    border-radius: 22px;
    background: linear-gradient(160deg, var(--kit-red), var(--kit-red-deep));
  }
  .task-card {
    position: absolute; left: 56px; top: 383px;
    width: 464px; height: 124px;
    background: var(--card-white);
    text-align: center; padding-top: 46px;
    font-size: 20px; color: var(--text-grey);
  }
  .action-button {
    position: absolute; left: 56px; width: 464px; height: 65px;
    border: none; border-radius: 3px;
    color: #fff; font-family: "Roboto", sans-serif;
    font-size: 25px; font-weight: 500;
    box-shadow: 0 2px 3px rgba(0,0,0,0.12);
  }
  .action-button.responses { top: 507px; background: var(--btn-green); border-radius: 0 0 3px 3px; }
  .action-button.drains { top: 592px; background: var(--btn-teal); }
  .action-button.antibiotics { top: 678px; background: var(--btn-blue); }
  .alarm-shortcut {
    position: absolute; left: 226px; top: 820px; width: 124px;
    text-align: center;
  }
  .alarm-shortcut .alarm-circle {
    width: 122px; height: 122px; border-radius: 50%;
    background: #fff; margin: 0 auto;
    box-shadow: 0 3px 8px rgba(0,0,0,0.12);
    display: flex; align-items: center; justify-content: center;
  }
  .alarm-shortcut .alarm-art {
    width: 72px; height: 72px; border-radius: 50%;
    background: linear-gradient(160deg, var(--clock-cream), var(--clock-green));
  }
  .alarm-shortcut .label {
    margin-top: 22px; font-size: 20px; color: var(--text-grey);
  }
</style>
</head>
<body>
  <main class="app-screen">
    <header class="status-bar">
      <svg width="28" height="22" viewBox="0 0 28 22" aria-hidden="true"><path d="M0 2 Q14 -4 28 2 L14 22 Z" fill="#fff"/></svg>
      <svg width="22" height="22" viewBox="0 0 22 22" aria-hidden="true"><path d="M22 0 V22 H0 Z" fill="#fff"/></svg>
      <svg width="14" height="22" viewBox="0 0 14 22" aria-hidden="true"><rect x="4" y="0" width="6" height="3" fill="#fff"/><rect x="0" y="2" width="14" height="20" rx="1" fill="#fff"/></svg>
      <span class="time">12:30</span>
    </header>

    <div class="care-kit-art" role="img" aria-label="Illustration of a red first aid case with an alarm clock emblem"></div>

    <section class="task-card">Nothing to do at the moment.</section>
    <button class="action-button responses">View Responses</button>
    <button class="action-button drains">Remind me to strip my drains</button>
    <button class="action-button antibiotics">Remind me to take my antibiotics</button>

    <div class="alarm-shortcut">
      <div class="alarm-circle">
        <div class="alarm-art" role="img" aria-label="Illustration of a green alarm clock"></div>
      </div>
      <p class="label">View Alarm</p>
    </div>
  </main>
</body>
</html>
```